institute for female grief councelors needs a design for its facebook group

Each year about 350.000 German women do have a misscarriage while they are pregnant. Their pain and grief is soul deep. Lots of them are stay still in grief even if they have got other children who are healthy and alive. Lots of these women have got difficulty in finally letting go pain, rage and grief. Some are even still in grief after more than twenty or thirty years of having lost their child through misscarriage!!!!

With this facebook group I want to give hope, trust and support as well as helpful advice in coping with this deep soul pain after having lost your child through misscarriage.

The facebook cover shall cause a great curiosity and fascination to the mothers so that they are interested in joining our facebook group.

At our institute women can book a-one-year-training to become a certified "Coach for WolkenHerzen" (grief councelor for women who are in deep grief after their misscarriage).

In Germany children who died through misscarriage are named "Sternenkind" (STARCHILD).
Therefore I want to have at least one shing star at the facebook cover symbolizing the still shining soullight of the dead child watching its mother who is still living on earth.

On the left side of the uploaded file you see the planet venus: symbol for mothers / female side of life.
The red sky colour symbolizes the colour of the uterus, the embryo's home before having died through misscarriage.
It ist also possible to include the silhoutte of a mother / several mothers looking up into the red / blue sky to watch the shining soullight of their dead child.

The facebook cover MUST include the following sentence:

Mama, ich lasse mein Licht für dich leuchten

(Mummy, I let my soullight shine for you)

Target Market(s)

German speaking mothers

Industry/Entity Type

coaching

Font styles to use
Script

Colors

Designer to choose colors to be used in the design.

Requirements
Must have
• golden fond writing, at least one shing star, silhouette of one / several mothers (no model typa - normal woman)
Nice to have
• planet venus - red background cover (like uterus colour)
Should not have
• mothers who like like a model or filmstar

```html
<!DOCTYPE html>
<html lang="de">
<head>
<meta charset="utf-8">
<title>Mama, ich lasse mein Licht für dich leuchten</title>
<link rel="stylesheet" href="https://fonts.googleapis.com/css2?family=Italiana&display=swap">
<style>
  :root {
    --night-deep: #141f35;
    --night: #1c2a44;
    --night-soft: #253552;
    --gold: #fde9a8;
    --gold-glow: #f2b84a;
    --moon-amber: #c98a35;
    --silver: #e9ecf4;
    --star-dot: rgba(233, 236, 244, 0.75);
    --cloud: #c3cccb;
    --cloud-soft: #7f8f9a;
    --vision-deep: #0f1838;
    --vision-mid: #28386f;
    --figure-blue: #5a6fc4;
    --figure-cream: #e8e4dc;
    --figure-rust: #b5553f;
  }
  * { margin: 0; padding: 0; box-sizing: border-box; }
  html, body { width: 1200px; height: 676px; overflow: hidden; background: var(--night-deep); }
  .cover {
    position: relative;
    width: 1200px;
    height: 676px;
    overflow: hidden;
    background: radial-gradient(ellipse at 40% 35%, var(--night-soft) 0%, var(--night) 45%, var(--night-deep) 100%);
  }
  .starfield {
    position: absolute;
    inset: 0;
    background-image:
      radial-gradient(circle, var(--star-dot) 0 1.2px, transparent 1.6px),
      radial-gradient(circle, var(--star-dot) 0 1px, transparent 1.4px),
      radial-gradient(circle, rgba(233, 236, 244, 0.5) 0 0.8px, transparent 1.2px);
    background-size: 97px 83px, 61px 71px, 43px 37px;
    background-position: 12px 20px, 40px 5px, 7px 31px;
  }
  .headline {
    position: absolute;
    left: 84px;
    top: 96px;
    width: 470px;
    text-align: center;
    font-family: "Italiana", serif;
    font-weight: 400;
    font-size: 56px;
    line-height: 47px;
    letter-spacing: 1.5px;
    color: var(--gold);
    text-shadow: 0 0 5px var(--gold-glow), 0 0 14px rgba(242, 184, 74, 0.65);
  }
  .headline span { display: block; white-space: nowrap; }
  .sparkle-pair { position: absolute; left: 46px; top: 194px; width: 46px; height: 48px; }
  .clouds {
    position: absolute;
    left: -40px;
    right: -40px;
    bottom: -40px;
    height: 300px;
    background:
      radial-gradient(ellipse at 12% 50%, rgba(195, 204, 203, 0.8) 0%, rgba(195, 204, 203, 0) 40%),
      radial-gradient(ellipse at 40% 75%, rgba(195, 204, 203, 0.75) 0%, rgba(195, 204, 203, 0) 48%),
      radial-gradient(ellipse at 78% 80%, rgba(195, 204, 203, 0.7) 0%, rgba(195, 204, 203, 0) 48%),
      linear-gradient(to bottom, rgba(127, 143, 154, 0) 0%, rgba(127, 143, 154, 0.6) 100%);
  }
  .vision {
    position: absolute;
    left: 662px;
    top: 99px;
    width: 502px;
    height: 524px;
    border-radius: 58% 42% 50% 50% / 40% 45% 55% 60%;
    background: linear-gradient(160deg, var(--vision-deep) 0%, var(--vision-mid) 60%, var(--cloud-soft) 100%);
    border: 1px solid rgba(233, 236, 244, 0.25);
    overflow: hidden;
  }
  .vision-figures {
    position: absolute;
    left: 165px;
    top: 183px;
    width: 315px;
    height: 345px;
    border-radius: 40% 40% 8px 8px / 30% 30% 8px 8px;
    background: linear-gradient(100deg, var(--figure-blue) 0%, var(--figure-blue) 55%, var(--figure-cream) 75%, var(--figure-rust) 100%);
    opacity: 0.85;
  }
  .orbit-ring {
    position: absolute;
    left: 1057px;
    top: 128px;
    width: 106px;
    height: 96px;
    border-radius: 50%;
    border: 1px solid rgba(233, 236, 244, 0.35);
    background: rgba(15, 24, 56, 0.55);
  }
  .moon { position: absolute; left: 606px; top: 84px; width: 196px; height: 200px; }
  .guiding-star { position: absolute; left: 738px; top: 56px; width: 100px; height: 96px; }
</style>
</head>
<body>
<main class="cover">
  <div class="starfield" aria-hidden="true"></div>

  <div class="vision">
    <div class="vision-figures" role="img" aria-label="Illustration: eine Mutter und ein Begleiter von hinten, die zu ihrem Sternenkind in den Himmel zeigen"></div>
  </div>
  <div class="orbit-ring"></div>

  <div class="clouds" role="img" aria-label="Weiche Nachtwolken am unteren Rand"></div>

  <svg class="moon" viewBox="0 0 196 200" aria-hidden="true">
    <defs>
      <filter id="moon-glow" x="-20%" y="-20%" width="140%" height="140%">
        <feGaussianBlur stdDeviation="3" result="b"/>
        <feMerge><feMergeNode in="b"/><feMergeNode in="SourceGraphic"/></feMerge>
      </filter>
    </defs>
    <path d="M120 14 A90 90 0 1 0 182 170 A72 72 0 1 1 120 14 Z" fill="var(--moon-amber)" opacity="0.75"/>
    <path d="M120 14 A90 90 0 1 0 182 170 A72 72 0 1 1 120 14 Z" fill="none" stroke="var(--silver)" stroke-width="3" filter="url(#moon-glow)"/>
    <path d="M108 24 A80 80 0 1 0 168 166 A64 64 0 1 1 108 24 Z" fill="none" stroke="var(--silver)" stroke-width="1.5" opacity="0.8"/>
  </svg>

  <svg class="guiding-star" viewBox="0 0 100 96" aria-hidden="true">
    <path d="M50 2 L53 44 L96 48 L53 52 L50 94 L47 52 L4 48 L47 44 Z" fill="var(--silver)"/>
    <path d="M82 16 L83 21 L88 22 L83 23 L82 28 L81 23 L76 22 L81 21 Z" fill="var(--silver)"/>
    <path d="M20 34 L21 38 L25 39 L21 40 L20 44 L19 40 L15 39 L19 38 Z" fill="var(--silver)"/>
    <path d="M68 70 L69 73 L72 74 L69 75 L68 78 L67 75 L64 74 L67 73 Z" fill="var(--silver)"/>
  </svg>

  <h1 class="headline">
    <span>Mama,</span>
    <span>ich lasse mein</span>
    <span>Licht für dich</span>
    <span>leuchten</span>
  </h1>

  <svg class="sparkle-pair" viewBox="0 0 46 48" aria-hidden="true">
    <path d="M16 2 Q18 18 30 20 Q18 22 16 38 Q14 22 2 20 Q14 18 16 2 Z" fill="none" stroke="var(--silver)" stroke-width="1.2"/>
    <path d="M36 30 Q37 38 44 39 Q37 40 36 47 Q35 40 28 39 Q35 38 36 30 Z" fill="none" stroke="var(--silver)" stroke-width="1"/>
  </svg>
</main>
</body>
</html>
```